Scrap Metal Recycling

We are looking for a simple yet bold business card. We already have the logo, please see attached. Color scheme of blue, black and white or just blue and white.

```html
<!DOCTYPE html>
<html lang="en">
<head>
<meta charset="UTF-8">
<title>Norvale Metals Co. – Business Card</title>
<link href="https://fonts.googleapis.com/css2?family=Montserrat:wght@400;500;700&display=swap" rel="stylesheet">
<style>
  :root {
    --backdrop: #e4e6e6;
    --brand-blue: #29a3c6;
    --brand-blue-deep: #1f8fb0;
    --ink: #2f3336;
    --paper: #ffffff;
    --paper-shade: #e6e6e6;
  }
  * { box-sizing: border-box; margin: 0; padding: 0; }
  html, body {
    width: 1200px; height: 800px; overflow: hidden;
    background: var(--backdrop);
    font-family: "Montserrat", sans-serif;
  }
  .canvas { position: relative; width: 1200px; height: 800px; }

  .card {
    position: absolute;
    background: var(--paper);
    box-shadow: 0 2px 4px rgba(0,0,0,0.18);
    overflow: hidden;
  }

  /* Front card */
  .card--front { left: 193px; top: 102px; width: 431px; height: 270px; }
  .front__band {
    position: absolute; left: 0; top: 0; width: 287px; height: 100%;
    background: linear-gradient(180deg, var(--brand-blue-deep) 0%, var(--brand-blue-deep) 30%, var(--brand-blue) 65%, var(--brand-blue) 100%);
    color: var(--paper);
  }
  .front__side {
    position: absolute; left: 287px; top: 0; right: 0; height: 100%;
    background: linear-gradient(180deg, var(--paper-shade) 0%, var(--paper-shade) 22%, var(--paper) 55%);
  }
  .front__wordmark {
    position: absolute; left: 0; right: 0; top: 36px;
    text-align: center;
    font-weight: 700; font-size: 10px; letter-spacing: 0.3px;
    color: var(--ink);
  }
  .holder__name {
    position: absolute; left: 30px; top: 98px;
    font-weight: 700; font-size: 21px; letter-spacing: 0.6px;
  }
  .holder__rule {
    position: absolute; left: 26px; top: 123px; width: 203px; height: 1px;
    background: var(--paper);
  }
  .holder__role {
    position: absolute; left: 32px; top: 127px;
    font-weight: 500; font-size: 10.5px; letter-spacing: 0.3px;
  }
  .contact-list {
    position: absolute; left: 26px; top: 176px; list-style: none;
  }
  .contact-list__item {
    display: flex; align-items: center; height: 15px;
    font-size: 8.6px; letter-spacing: 0.2px;
  }
  .contact-list__icon { width: 10px; height: 10px; margin-right: 5px; flex: none; }

  /* Back card */
  .card--back { left: 567px; top: 423px; width: 441px; height: 276px; }
  .back__band {
    position: absolute; right: 0; top: 0; width: 148px; height: 100%;
    background: var(--brand-blue);
  }
  .back__wordmark {
    position: absolute; left: 0; width: 293px; top: 124px;
    text-align: center;
    font-weight: 700; font-size: 21px; letter-spacing: 0.5px;
    color: var(--ink);
  }
</style>
</head>
<body>
<main class="canvas">

  <section class="card card--front" aria-label="Business card front">
    <div class="front__band">
      <h1 class="holder__name">NAME SURNAME</h1>
      <div class="holder__rule"></div>
      <p class="holder__role">Job Position</p>
      <ul class="contact-list">
        <li class="contact-list__item">
          <svg class="contact-list__icon" viewBox="0 0 10 10"><path d="M5 0.5a3 3 0 0 1 3 3c0 2.2-3 6-3 6s-3-3.8-3-6a3 3 0 0 1 3-3z" fill="#fff"/><circle cx="5" cy="3.5" r="1.1" fill="#1f8fb0"/></svg>
          Company address line
        </li>
        <li class="contact-list__item">
          <svg class="contact-list__icon" viewBox="0 0 10 10"><path d="M2.2 0.8l1.6 1.8-0.9 1.2c0.6 1.3 1.6 2.3 2.9 2.9l1.2-0.9 1.8 1.6-0.9 1.6C4.6 9 1 5.4 0.9 1.7z" fill="#fff"/></svg>
          +12 345 678 90
        </li>
        <li class="contact-list__item">
          <svg class="contact-list__icon" viewBox="0 0 10 10"><rect x="0.5" y="2" width="9" height="6" fill="#fff"/><path d="M0.8 2.3L5 5.5l4.2-3.2" fill="none" stroke="#1f8fb0" stroke-width="0.8"/></svg>
          email@yourcompany.com
        </li>
        <li class="contact-list__item">
          <svg class="contact-list__icon" viewBox="0 0 10 10" fill="none" stroke="#fff" stroke-width="0.8"><circle cx="5" cy="5" r="4.2"/><ellipse cx="5" cy="5" rx="1.8" ry="4.2"/><path d="M0.8 5h8.4M1.6 2.8h6.8M1.6 7.2h6.8"/></svg>
          www.yourwebsite.com
        </li>
      </ul>
    </div>
    <div class="front__side">
      <p class="front__wordmark">NORVALE METALS CO.</p>
    </div>
  </section>

  <section class="card card--back" aria-label="Business card back">
    <p class="back__wordmark">NORVALE METALS CO.</p>
    <div class="back__band"></div>
  </section>

</main>
</body>
</html>
```